IT Services Business Card Design

We require a business card design for an IT services company called RT Program Freightworks.

We specialize in taking an organisations software and readying it for deployment to new environments (e.g. Zen qa to Zen 4). This process is termed application packaging. This is not the same as putting things in boxes but I am happy to use boxes as a pun icon ;-) This is our second step in branding, we currently have a new logo and our poor excuse of a website is next to be updated but it contains information on who we are and what we cover at rtprogramfreightworks.example

We are looking for a fun, modern but stylish and professional looking design.

I have attached the logo in multiple formats including vector formats (and the fonts that created the logo if required)
Updates

Thanks to all the designers so far, some great designs in there.  I will be selecting a card design on the deadline date. 

However, there is still time to submit some more designs.  The majority of the ones I have so far are typical simplistic designs that we have all seen before and I have enough of those to choose from now.  If you wish to submit any more designs, please submit somthing unusual to grab our attention.

Target Market(s)

Project executives of large organisations looking for Panecraft migrations

Industry/Entity Type

Software

Requirements
Must have
• Want to show company name, contact name, title, main number, contact number, fax number, email address and website address. I do not want to show the address.
Must use the attached logo, retaining the colours in them.

This has to be a double-sided design. I will be using lark.example and will be selecting their rounded corner business card design.

Their templates and design requirements (sizing etc.) can be found here: http://uk.lark.example/help/faq/templates-and-guidelines.html

Happy for company name or website to be on either side of the card.

This design has to be original and not used before for another company

Would like to style it around the business colours in the logo
Nice to have
• Lark.example has an option for multiple card designs to appear on the back. If this is possible in the budget and time you have and you have a design(s) that work with that but carry the same style and theme, that would be nice to see but not necessary.
Should not have
• We do not want to put a postal address on the cards

```html
<!DOCTYPE html>
<html lang="en">
<head>
<meta charset="utf-8">
<title>RT Program Freightworks – Business Card</title>
<link rel="stylesheet" href="https://fonts.googleapis.com/css2?family=Jost:wght@400;500;600&display=swap">
<style>
  :root {
    --page-bg: #ecebe8;
    --card-white: #ffffff;
    --brand-blue: #3a6fdc;
    --brand-blue-deep: #2f5fcf;
    --brand-blue-light: #b9cdf5;
    --brand-grey: #5f5a55;
    --text-white: #ffffff;
    --card-shadow: rgba(0, 0, 0, 0.18);
  }
  * { box-sizing: border-box; margin: 0; padding: 0; }
  html, body {
    width: 1200px; height: 864px; overflow: hidden;
    background: var(--page-bg);
    font-family: "Jost", "Futura", sans-serif;
  }
  .canvas {
    position: relative; width: 1200px; height: 864px;
  }
  .card {
    position: absolute; top: 257px;
    width: 540px; height: 350px;
    border-radius: 26px; overflow: hidden;
    box-shadow: 0 10px 26px var(--card-shadow);
  }
  .card-front { left: 45px; background: var(--card-white); }
  .card-back {
    left: 615px;
    background: radial-gradient(circle at 48% 42%, #c7d8fb 0%, #7fa2ee 30%, var(--brand-blue) 62%, var(--brand-blue-deep) 100%);
  }
  .front-swoosh { position: absolute; inset: 0; width: 100%; height: 100%; }

  .brand-lockup {
    position: absolute; left: 38px; top: 52px;
    display: flex; align-items: center; gap: 14px;
  }
  .brand-mark {
    width: 30px; height: 30px; border-radius: 50%;
    background: var(--brand-blue);
  }
  .brand-name {
    font-size: 30px; font-weight: 400; line-height: 1.05;
    color: var(--brand-grey); letter-spacing: 0.2px;
  }

  .holder { position: absolute; left: 60px; top: 198px; }
  .holder-name { font-size: 22px; font-weight: 600; color: var(--brand-blue); }
  .holder-title { font-size: 15px; font-weight: 400; color: var(--brand-grey); margin-top: 2px; }

  .contact-list {
    position: absolute; right: 26px; top: 166px;
    list-style: none; text-align: right;
    color: var(--text-white); font-size: 14.5px; line-height: 21px;
  }
  .contact-list li { display: flex; justify-content: flex-end; align-items: center; gap: 7px; }
  .contact-icon { width: 11px; height: 11px; fill: var(--text-white); flex: none; }

  .back-brand {
    position: absolute; left: 0; right: 0; top: 128px;
    display: flex; justify-content: center; align-items: center; gap: 16px;
  }
  .back-brand .brand-mark { width: 40px; height: 40px; background: var(--text-white); }
  .back-brand .brand-name { font-size: 34px; color: var(--text-white); }
  .back-url {
    position: absolute; left: 0; right: 0; bottom: 44px;
    text-align: center; color: var(--text-white);
    font-size: 15px; letter-spacing: 3.5px;
  }
</style>
</head>
<body>
<main class="canvas">

  <section class="card card-front" aria-label="Card front">
    <svg class="front-swoosh" viewBox="0 0 540 350" aria-hidden="true">
      <defs>
        <linearGradient id="swooshFill" x1="0" y1="1" x2="1" y2="0">
          <stop offset="0" stop-color="#e4ecfc"/>
          <stop offset="0.45" stop-color="#8fb0f0"/>
          <stop offset="1" stop-color="#3a6fdc"/>
        </linearGradient>
      </defs>
      <path d="M0,350 L0,338 C140,320 240,260 320,190 C390,130 460,110 540,104 L540,350 Z" fill="url(#swooshFill)"/>
      <path d="M0,326 C150,306 250,246 325,178 C392,120 460,98 540,92" fill="none" stroke="#5f5a55" stroke-width="4"/>
      <path d="M0,313 C150,292 260,226 330,162 C395,106 462,86 540,80" fill="none" stroke="#3a6fdc" stroke-width="5"/>
      <path d="M0,300 C120,288 205,258 265,222" fill="none" stroke="#3a6fdc" stroke-width="3"/>
    </svg>

    <div class="brand-lockup">
      <span class="brand-mark"></span>
      <span class="brand-name">RT Program<br>Freightworks</span>
    </div>

    <div class="holder">
      <p class="holder-name">Your Name</p>
      <p class="holder-title">Title</p>
    </div>

    <ul class="contact-list">
      <li><svg class="contact-icon" viewBox="0 0 12 12"><path d="M2 1h2l1 3-1.3 1a7 7 0 0 0 3.3 3.3L8 7l3 1v2a1 1 0 0 1-1 1A9 9 0 0 1 1 2a1 1 0 0 1 1-1z"/></svg>0100 200300</li>
      <li><svg class="contact-icon" viewBox="0 0 12 12"><path d="M3.5 0h5a1 1 0 0 1 1 1v10a1 1 0 0 1-1 1h-5a1 1 0 0 1-1-1V1a1 1 0 0 1 1-1zm.5 1.5v7h4v-7zM6 9.5a.8.8 0 1 0 0 1.6.8.8 0 0 0 0-1.6z"/></svg>0100 200300</li>
      <li><svg class="contact-icon" viewBox="0 0 12 12"><path d="M3 0h6v3H3zM1 4h10a1 1 0 0 1 1 1v4H10v3H2V9H0V5a1 1 0 0 1 1-1zm2 5v2h6V9z"/></svg>0100 200300</li>
      <li><svg class="contact-icon" viewBox="0 0 12 12"><path d="M0 2h12v8H0zM1 3l5 4 5-4z" fill-rule="evenodd"/></svg>info@rtprogramfreightworks.example</li>
      <li><svg class="contact-icon" viewBox="0 0 12 12"><path d="M6 0a6 6 0 1 0 0 12A6 6 0 0 0 6 0zm0 1.2c.8.9 1.3 2.6 1.4 4.2H4.6C4.7 3.8 5.2 2.1 6 1.2zM4.6 6.6h2.8c-.1 1.6-.6 3.3-1.4 4.2-.8-.9-1.3-2.6-1.4-4.2z" fill-rule="evenodd"/></svg>www.rtprogramfreightworks.example</li>
    </ul>
  </section>

  <section class="card card-back" aria-label="Card back">
    <div class="back-brand">
      <span class="brand-mark"></span>
      <span class="brand-name">RT Program Freightworks</span>
    </div>
    <p class="back-url">www.rtprogramfreightworks.example</p>
  </section>

</main>
</body>
</html>
```